Update our business cards to match our awesome new website

Need a new design for company business cards. We have recently revamped our website and would like our business cards to get a refresh too. I've uploaded the company artwork, logo, as well as the Branding Deck to better understand the look & feel of our brand. Please visit the website at bellcrestholdingsoh.com.

Industry/Entity Type

Real Estate

Contact Information for Business Card

must use the colors outlined in the Branding Deck uploaded to the site, or the colors of our logo.

Font styles to use
Other font styles liked:
• Calibri

Requirements
Must have
• Required items: Name, title, company logo, address: 217 Fennimore Ave. Suite 300, Lakeport, OH 44093, email address: glen@bellcrestholdingsOH.com, company phone 800-555-0172, cell: 216-555-0148
Nice to have
• a more simple design. not complicated
Should not have
• cartoonish characters, or whimsical writing or artwork, stay within our branding colors

```html
<!DOCTYPE html>
<html lang="en">
<head>
<meta charset="utf-8">
<title>Bellcrest Holdings – Business Cards</title>
<link href="https://fonts.googleapis.com/css2?family=Carlito:wght@400;700&display=swap" rel="stylesheet">
<style>
  :root {
    --backdrop: #d9d8d5;
    --card: #161616;
    --white: #ffffff;
    --green: #7cc242;
    --green-deep: #4e9a3a;
    --orange: #f26b21;
    --font: "Carlito", "Calibri", sans-serif;
  }
  * { box-sizing: border-box; margin: 0; padding: 0; }
  html, body { width: 1200px; height: 938px; overflow: hidden; }
  body {
    background: var(--backdrop);
    font-family: var(--font);
    color: var(--white);
    display: flex;
    flex-direction: column;
    align-items: center;
    justify-content: center;
    gap: 44px;
  }
  .card {
    position: relative;
    width: 680px;
    height: 389px;
    background: var(--card);
    overflow: hidden;
  }

  /* Front */
  .brand {
    position: absolute;
    left: 60px;
    top: 46px;
    display: flex;
    align-items: center;
    gap: 14px;
  }
  .brand-dot {
    width: 22px; height: 22px;
    border-radius: 50%;
    background: var(--green);
  }
  .brand-name {
    font-size: 34px;
    font-weight: 400;
    letter-spacing: 1.5px;
    color: var(--white);
  }
  .person {
    position: absolute;
    left: 60px;
    top: 170px;
    width: 250px;
  }
  .person-name {
    font-size: 28px;
    font-weight: 700;
    letter-spacing: 1px;
    text-transform: uppercase;
  }
  .person-title {
    font-size: 22px;
    color: var(--green);
    margin-top: 4px;
  }
  .divider {
    position: absolute;
    left: 320px;
    top: 150px;
    width: 2px;
    height: 118px;
    background: var(--green);
  }
  .contacts {
    position: absolute;
    left: 342px;
    top: 146px;
    list-style: none;
    display: flex;
    flex-direction: column;
    gap: 6px;
  }
  .contacts li {
    display: flex;
    align-items: center;
    gap: 10px;
    font-size: 19px;
    letter-spacing: 0.3px;
  }
  .contacts svg { width: 18px; height: 18px; flex: none; }
  .address-band {
    position: absolute;
    left: 0; right: 0; bottom: 36px;
    height: 44px;
    background: linear-gradient(90deg, var(--green-deep), var(--green));
    display: flex;
    align-items: center;
    justify-content: center;
    font-size: 20px;
    letter-spacing: 0.5px;
  }

  /* Back */
  .card-back {
    display: flex;
    flex-direction: column;
    align-items: center;
    justify-content: center;
    gap: 56px;
  }
  .card-back .brand { position: static; }
  .card-back .brand-dot { width: 30px; height: 30px; }
  .card-back .brand-name { font-size: 46px; }
  .website { font-size: 22px; letter-spacing: 1px; }
  .website .domain { color: var(--green); }
</style>
</head>
<body>

  <section class="card card-front" aria-label="Business card front">
    <div class="brand">
      <span class="brand-dot"></span>
      <span class="brand-name">Bellcrest Holdings of Ohio, LLC</span>
    </div>

    <div class="person">
      <p class="person-name">Daniel Hartwell</p>
      <p class="person-title">General Manager</p>
    </div>

    <div class="divider"></div>

    <ul class="contacts">
      <li>
        <svg viewBox="0 0 24 24" aria-hidden="true"><path fill="var(--orange)" d="M6.6 10.8a15.1 15.1 0 0 0 6.6 6.6l2.2-2.2c.3-.3.7-.4 1-.2 1.1.4 2.3.6 3.6.6.6 0 1 .4 1 1V20c0 .6-.4 1-1 1A17 17 0 0 1 3 4c0-.6.4-1 1-1h3.5c.6 0 1 .4 1 1 0 1.3.2 2.5.6 3.6.1.3 0 .7-.2 1z"/></svg>
        800-555-0172
      </li>
      <li>
        <svg viewBox="0 0 24 24" aria-hidden="true"><rect x="6" y="2" width="12" height="20" rx="2" fill="none" stroke="var(--orange)" stroke-width="2"/><circle cx="12" cy="18" r="1.2" fill="var(--orange)"/></svg>
        216-555-0148
      </li>
      <li>
        <svg viewBox="0 0 24 24" aria-hidden="true"><rect x="2" y="5" width="20" height="14" rx="1" fill="var(--orange)"/><path d="M2 6l10 7 10-7" fill="none" stroke="var(--card)" stroke-width="1.6"/></svg>
        glen@bellcrestholdingsOH.com
      </li>
      <li>
        <svg viewBox="0 0 24 24" aria-hidden="true"><circle cx="12" cy="12" r="9.5" fill="none" stroke="var(--orange)" stroke-width="2"/><ellipse cx="12" cy="12" rx="4" ry="9.5" fill="none" stroke="var(--orange)" stroke-width="1.6"/><path d="M2.5 12h19" stroke="var(--orange)" stroke-width="1.6"/></svg>
        www.bellcrestholdingsoh.com
      </li>
    </ul>

    <div class="address-band">217 Fennimore Ave. Suite 300, Lakeport, OH 44093</div>
  </section>

  <section class="card card-back" aria-label="Business card back">
    <div class="brand">
      <span class="brand-dot"></span>
      <span class="brand-name">Bellcrest Holdings of Ohio, LLC</span>
    </div>
    <p class="website">www.<span class="domain">bellcrestholdingsoh</span>.com</p>
  </section>

</body>
</html>
```